Artificial intelligence, machine learning, and automation company needs a sexy business card design

We need a sleek and sexy business card design for an AI consulting company based in Philadelphia PA. We provide custom machine learning and automation solutions for companies of all shapes and sizes. The primary industries that we serve are pharmaceuticals, engineering, healthcare, and computer software. We would like the designs to be a black business card that uses green as a sleek accent color. The final design should communicate intelligence, cutting edge new-tech, and optimization.

Target Market(s)

C-level and VP level executives of multi-million annual companies. Mostly in Pharma, Healthcare, Real Estate, Retail, and Engineering

Industry/Entity Type

Computer Software

Contact Information for Business Card

Name: Jack Moss
Title: CEO
Cell: 215 604 8293
Email: JackM@quillarcworks.example
Website: www.QuillarcWorks.example

Font styles to use
Sans Serif

Colors

Designer to choose colors to be used in the design.

Requirements
Must have
• 1) Attached Quillarc Logo (either with colors or not/embossed)
• 2) "Artificial Intelligence" "Automation" and "Machine Learning"
• 3) "Quillarc Laboratories" or "Quillarc Works" or "Quillarc"
• 4) Sexy AF.
Nice to have
• Black card / dark card color, "Quillarc Green" accent colors (in attached .ai file), Embossment of logo/name/etc, thick card stock, colored borders (on card sides, not front/back faces)
Should not have
• Should not be bland, or unsexy.

```html
<!DOCTYPE html>
<html lang="en">
<head>
<meta charset="utf-8">
<title>Quillarc Laboratories – Business Card</title>
<link rel="stylesheet" href="https://fonts.googleapis.com/css2?family=Roboto:wght@400;500&display=swap">
<style>
  :root {
    --page-bg: #e8e8e5;
    --card-black: #1f1f20;
    --pattern-dark: #2c2c2e;
    --text-white: #f4f4f4;
    --brand-grey: #707073;
    --quillarc-green: #4f8e8b;
  }
  * { box-sizing: border-box; margin: 0; padding: 0; }
  html, body {
    width: 1200px;
    height: 800px;
    overflow: hidden;
    background: var(--page-bg);
    font-family: "Roboto", Arial, sans-serif;
  }
  .card-sheet {
    position: relative;
    width: 1200px;
    height: 800px;
    display: flex;
    justify-content: center;
    align-items: center;
    gap: 40px;
  }
  .card {
    position: relative;
    width: 540px;
    height: 309px;
    background: var(--card-black);
    overflow: hidden;
    box-shadow: 0 6px 18px rgba(0, 0, 0, 0.18);
  }

  /* Contact side */
  .texture-field {
    position: absolute;
    left: 0;
    top: 0;
    width: 330px;
    height: 120px;
    background: linear-gradient(160deg, var(--pattern-dark) 0%, rgba(44, 44, 46, 0.6) 45%, rgba(31, 31, 32, 0) 80%);
  }
  .contact-block {
    position: absolute;
    left: 320px;
    top: 148px;
    color: var(--text-white);
  }
  .contact-name {
    font-size: 21px;
    font-weight: 400;
    letter-spacing: 0.2px;
    margin-bottom: 12px;
  }
  .contact-list { list-style: none; }
  .contact-list li {
    display: flex;
    align-items: center;
    gap: 11px;
    font-size: 13px;
    line-height: 1.25;
    margin-bottom: 6px;
  }
  .contact-icon {
    width: 12px;
    height: 12px;
    flex: none;
  }

  /* Brand side */
  .corner-accent {
    position: absolute;
    right: 0;
    top: 0;
    width: 70px;
    height: 62px;
  }
  .brand-lockup {
    position: absolute;
    left: 0;
    right: 0;
    top: 105px;
    display: flex;
    flex-direction: column;
    align-items: center;
    color: var(--brand-grey);
    font-weight: 500;
  }
  .brand-mark {
    width: 44px;
    height: 44px;
    border: 3px solid var(--brand-grey);
    margin-bottom: 10px;
  }
  .brand-name {
    font-size: 20px;
    letter-spacing: 5px;
    line-height: 1;
  }
  .brand-sub {
    font-size: 8.5px;
    letter-spacing: 2.6px;
    margin-top: 3px;
  }
</style>
</head>
<body>
  <main class="card-sheet">
    <section class="card card--contact">
      <div class="texture-field" role="img" aria-label="Fading field of small embossed triangle pattern"></div>
      <div class="contact-block">
        <h1 class="contact-name">Jack Moss | CEO</h1>
        <ul class="contact-list">
          <li>
            <svg class="contact-icon" viewBox="0 0 12 12" aria-hidden="true">
              <circle cx="6" cy="6" r="5.4" fill="none" stroke="#f4f4f4" stroke-width="1"/>
              <path d="M4 3.2 L5 3 L5.6 4.6 L5 5.1 Q5.6 6.5 6.9 7 L7.4 6.4 L9 7 L8.8 8 Q6.8 8.6 5 7 Q3.4 5.2 4 3.2 Z" fill="#f4f4f4"/>
            </svg>
            <span>215 604 8293</span>
          </li>
          <li>
            <svg class="contact-icon" viewBox="0 0 12 12" aria-hidden="true">
              <circle cx="6" cy="6" r="6" fill="#f4f4f4"/>
              <rect x="3" y="4" width="6" height="4.2" fill="#1f1f20"/>
              <path d="M3 4 L6 6.4 L9 4" fill="none" stroke="#f4f4f4" stroke-width="0.8"/>
            </svg>
            <span>JackM@quillarcworks.example</span>
          </li>
          <li>
            <svg class="contact-icon" viewBox="0 0 12 12" aria-hidden="true">
              <circle cx="6" cy="6" r="5.4" fill="none" stroke="#f4f4f4" stroke-width="1"/>
              <ellipse cx="6" cy="6" rx="2.3" ry="5.4" fill="none" stroke="#f4f4f4" stroke-width="0.9"/>
              <path d="M0.8 6 H11.2" stroke="#f4f4f4" stroke-width="0.9"/>
            </svg>
            <span>www.QuillarcWorks.example</span>
          </li>
        </ul>
      </div>
    </section>

    <section class="card card--brand">
      <svg class="corner-accent" viewBox="0 0 70 62" aria-hidden="true">
        <polygon points="0,0 70,0 70,62" fill="var(--quillarc-green)"/>
      </svg>
      <div class="brand-lockup">
        <span class="brand-mark" aria-hidden="true"></span>
        <span class="brand-name">QUILLARC</span>
        <span class="brand-sub">LABORATORIES</span>
      </div>
    </section>
  </main>
</body>
</html>
```